Product label for herbal salves, lotions, soaps and tinctures

We need a very simple, clean and organic looking label that can be used for an ointment jar, a lotion bottle and a dropper bottle.
We have an existing logo (see attached). We like the colors white, olive green, gold and black. It needs to include product name as dominant and logo. It also needs to include an ingredient list, and usage statement. Include weight of product, distributed by, made in the USA, and QRB statement.
Example of what needs to be present:
Logo
Name: Sunward Blend Tonic
Used for: For Muscle Aches, Arthritis, Tendonitis, Headaches
To Use: For muscle aches, arthritis and tendonitis, massage into affected area. For tension headache apply to neck, temples and forehead.
Store in a cool and dry place, away from direct heat and sunlight.
Weight of product: 1.75
DIST. BY: Brightmoor Herbal
Made in the USA
This product is not intended to diagnose, treat, cure
or prevent any disease. Not regulated
by the QRB. Please consult your health care practitioner
before using product. Discontinue use if any adverse reaction occurs.
Ingredient list:
Wildcrafted Ingredients:
Ashwagandha Root, Peppermint Leaf, Hops Flowers, St. John’s Wort Herb, Arnica Flowers, Green Tea Leaf, Alfalfa Leaf, Dandelion Root, Burdock Root, Chickweed Herb, Chaparral Leaf, Yarrow Flowers, Boneset Herb, Moringa Leaf, Meadowsweet Herb, Nettle Leaf
Organic Ingredients:
Olive Oil, Aloe Leaf, Sweet Birch Bark, Helichrysum Flowers, Holy Basil Leaf, Borage Herb, Ginger Root, Angelica Root, White Willow Bark, Mustard Seed, Beeswax, Vitamin E, Essential Oils
Dimensions of Jar:
Circumference: 7 in.
Height: 1 in.

```html
<!DOCTYPE html>
<html lang="en">
<head>
<meta charset="utf-8">
<title>Brightmoor Herbal — Sunward Blend Tonic Labels</title>
<link rel="stylesheet" href="https://fonts.googleapis.com/css2?family=Kaushan+Script&family=Lato:wght@400;700&family=Oswald:wght@300&family=Roboto+Condensed:wght@400;700&display=swap">
<style>
  :root {
    --page: #0d0d0d;
    --label: #050505;
    --gold: #d8962a;
    --olive: #6b7530;
    --white: #f4f1ea;
  }
  * { box-sizing: border-box; margin: 0; padding: 0; }
  html, body { width: 720px; height: 1200px; overflow: hidden; background: var(--page); }
  .canvas { position: relative; width: 720px; height: 1200px; }

  .label {
    position: absolute; left: 80px; width: 560px; height: 560px;
    border-radius: 50%; background: var(--label);
    box-shadow: 0 0 0 1px #1c1c1c;
  }
  .label--front { top: 24px; }
  .label--back { top: 616px; }
  .label__ring { position: absolute; inset: 0; }
  .label__body {
    position: absolute; inset: 0; display: flex; flex-direction: column;
    align-items: center; text-align: center;
  }

  .brand {
    font-family: 'Lato', sans-serif; font-weight: 700; color: var(--olive);
    font-size: 20px; line-height: 26px; letter-spacing: 0.5px;
    display: flex; align-items: center; gap: 7px;
  }
  .brand__dot { width: 9px; height: 9px; border-radius: 50%; background: var(--olive); }

  .product { font-weight: 400; }
  .product__script { display: block; font-family: 'Kaushan Script', cursive; font-weight: 400; color: var(--gold); line-height: 1; }
  .product__main { display: block; font-family: 'Oswald', sans-serif; font-weight: 300; color: var(--olive); line-height: 0.95; }
  .uses {
    font-family: 'Lato', sans-serif; font-weight: 400; color: var(--white); text-transform: uppercase;
    line-height: 1.25;
  }
  .uses__dot { color: var(--gold); }

  .ingredients { font-family: 'Roboto Condensed', sans-serif; line-height: 1.4; }
  .ingredients__title { font-weight: 700; }

  /* front */
  .label--front .label__body { padding-top: 30px; }
  .label--front .product__script { font-size: 38px; margin-top: 6px; }
  .label--front .product__main { font-size: 108px; margin-top: 0; }
  .label--front .uses { font-size: 18px; letter-spacing: 4.5px; margin-top: 6px; }
  .label--front .ingredients { color: var(--gold); font-size: 9.5px; width: 400px; margin-top: 14px; }
  .label--front .ingredients__group + .ingredients__group { margin-top: 10px; }
  .weight { font-family: 'Lato', sans-serif; color: var(--olive); font-size: 23px; margin-top: 12px; }
  .origin { font-family: 'Lato', sans-serif; color: var(--gold); font-size: 13px; margin-top: 6px; }

  /* back */
  .label--back .label__body { padding-top: 66px; }
  .label--back .product__script { font-size: 26px; }
  .label--back .product__main { font-size: 66px; }
  .label--back .uses { font-size: 12px; letter-spacing: 3.5px; margin-top: 4px; }
  .directions {
    font-family: 'Roboto Condensed', sans-serif; color: var(--white);
    font-size: 8px; line-height: 1.4; width: 420px; margin-top: 10px;
  }
  .directions strong { font-weight: 700; }
  .label--back .ingredients { color: var(--white); font-size: 8px; width: 400px; margin-top: 9px; }
  .label--back .ingredients__group + .ingredients__group { margin-top: 7px; }
  .distributor { font-family: 'Roboto Condensed', sans-serif; color: var(--white); font-size: 7.5px; margin-top: 8px; }
  .badges { display: flex; gap: 130px; margin-top: 8px; }
  .badge { width: 40px; height: 40px; border-radius: 50%; background: var(--white); border: 3px solid #333; }
</style>
</head>
<body>
<main class="canvas">

  <section class="label label--front">
    <svg class="label__ring" viewBox="0 0 560 560" aria-hidden="true">
      <path d="M 140 80 A 244 244 0 1 0 420 80" fill="none" stroke="var(--gold)" stroke-width="3"/>
    </svg>
    <div class="label__body">
      <div class="brand"><span class="brand__dot"></span>Brightmoor Herbal</div>
      <h1 class="product">
        <span class="product__script">Sunward Blend</span>
        <span class="product__main">Tonic</span>
      </h1>
      <p class="uses">For Muscle Aches <span class="uses__dot">•</span> Arthritis<br>Tendonitis <span class="uses__dot">•</span> Headaches</p>
      <div class="ingredients">
        <div class="ingredients__group">
          <p class="ingredients__title">Wildcrafted Ingredients:</p>
          <p>Ashwagandha Root, Peppermint Leaf, Hops Flowers, St. John’s Wort Herb, Arnica Flowers, Green Tea Leaf, Alfalfa Leaf, Dandelion Root, Burdock Root, Chickweed Herb, Chaparral Leaf, Yarrow Flowers, Boneset Herb, Moringa Leaf, Meadowsweet Herb, Nettle Leaf</p>
        </div>
        <div class="ingredients__group">
          <p class="ingredients__title">Organic Ingredients:</p>
          <p>Olive Oil, Aloe Leaf, Sweet Birch Bark, Helichrysum Flowers, Holy Basil Leaf, Borage Herb, Ginger Root, Angelica Root, White Willow Bark, Mustard Seed, Beeswax, Vitamin E, Essential Oils</p>
        </div>
      </div>
      <p class="weight">1.75oz | 50gr</p>
      <p class="origin">MADE IN USA</p>
    </div>
  </section>

  <section class="label label--back">
    <svg class="label__ring" viewBox="0 0 560 560" aria-hidden="true">
      <circle cx="280" cy="280" r="244" fill="none" stroke="var(--gold)" stroke-width="3"/>
    </svg>
    <div class="label__body">
      <h2 class="product">
        <span class="product__script">Sunward Blend</span>
        <span class="product__main">Tonic</span>
      </h2>
      <p class="uses">For Muscle Aches <span class="uses__dot">•</span> Arthritis<br>Tendonitis <span class="uses__dot">•</span> Headaches</p>
      <div class="directions">
        <p><strong>Used for:</strong> For Muscle Aches, Arthritis, Tendonitis, Headaches</p>
        <p><strong>To Use:</strong> For muscle aches, arthritis and tendonitis, massage into affected area. For tension headache apply to neck, temples and forehead.</p>
        <p>Store in a cool and dry place, away from direct heat and sunlight.</p>
        <p>This product is not intended to diagnose, treat, cure or prevent any disease. Not regulated by the QRB. Please consult your health care practitioner before using product. Discontinue use if any adverse reaction occurs.</p>
      </div>
      <div class="ingredients">
        <div class="ingredients__group">
          <p class="ingredients__title">Wildcrafted Ingredients:</p>
          <p>Ashwagandha Root, Peppermint Leaf, Hops Flowers, St. John’s Wort Herb, Arnica Flowers, Green Tea Leaf, Alfalfa Leaf, Dandelion Root, Burdock Root, Chickweed Herb, Chaparral Leaf, Yarrow Flowers, Boneset Herb, Moringa Leaf, Meadowsweet Herb, Nettle Leaf</p>
        </div>
        <div class="ingredients__group">
          <p class="ingredients__title">Organic Ingredients:</p>
          <p>Olive Oil, Aloe Leaf, Sweet Birch Bark, Helichrysum Flowers, Holy Basil Leaf, Borage Herb, Ginger Root, Angelica Root, White Willow Bark, Mustard Seed, Beeswax, Vitamin E, Essential Oils</p>
        </div>
      </div>
      <p class="distributor">Manufactured and Distributed by Brightmoor Herbal</p>
      <div class="badges">
        <span class="badge" role="img" aria-label="Natural product badge"></span>
        <span class="badge" role="img" aria-label="Made in USA badge"></span>
      </div>
    </div>
  </section>

</main>
</body>
</html>
```